Trevlo Home Buyers

We need a website designed for the a house buying company. It can look and feel similar to a real estate agency, but the messaging is different. Attached in the document below you will see what we are looking for. The main thing we are going for is clean, corporate and approachable. The Logo files are also attached. We want to use the logo and branding throughout the site.

```html
<!DOCTYPE html>
<html lang="en">
<head>
<meta charset="utf-8">
<title>Trevlo Home Buyers</title>
<link href="https://fonts.googleapis.com/css2?family=Varela+Round&display=swap" rel="stylesheet">
<style>
:root{
  --blue:#1b4f91;
  --blue-dark:#123c70;
  --green:#6bb02a;
  --ink:#1e1e1e;
  --muted:#555;
  --line:#cfcfcf;
  --band:#ececec;
  --footer:#e4e4e4;
  --white:#fff;
}
*{box-sizing:border-box;margin:0;padding:0}
html,body{width:1200px;height:5000px;overflow:hidden;background:var(--white)}
body{position:relative;font-family:"Varela Round",Arial,sans-serif;color:var(--ink)}
.abs{position:absolute}
.center{left:0;width:1200px;text-align:center}
h1,h2{font-weight:400}
.section-title{font-size:27px;color:var(--ink)}
.section-sub{font-size:15px;color:var(--ink)}
.btn{position:absolute;background:var(--blue);color:var(--white);border-radius:20px;font-size:10px;display:flex;align-items:center;justify-content:center;box-shadow:0 3px 6px rgba(0,0,0,.25);letter-spacing:.2px}

/* header */
.site-header{left:0;top:0;width:1200px;height:92px;background:var(--white)}
.brand{display:flex;align-items:center;gap:8px}
.brand-name{font-size:36px;color:var(--blue);letter-spacing:-1px;line-height:1}
.brand-tag{font-size:11px;color:var(--blue);letter-spacing:3px}
.brand-mark{width:14px;height:14px;background:var(--green);border-radius:50%}
.top-phone{right:232px;top:24px;font-size:10px;color:var(--blue);display:flex;gap:5px;align-items:center}
.main-nav{right:232px;top:54px;display:flex;gap:14px;font-size:10px}

/* hero */
.hero{left:0;top:92px;width:1200px;height:533px;background:linear-gradient(180deg,#5b8bc2 0%,#8aa7c2 40%,#7c8470 70%,#4d5b3d 100%)}
.hero-title{top:276px;font-size:34px;color:var(--white);text-shadow:0 2px 4px rgba(0,0,0,.4)}
.hero-sub{top:343px;font-size:19px;color:var(--white)}
.address-field{left:325px;top:400px;width:340px;height:37px;border:3px solid var(--green);border-radius:20px;background:rgba(20,40,70,.55);color:var(--white);font-size:12px;display:flex;align-items:center;padding-left:26px;gap:14px}
.offer-btn{left:688px;top:400px;width:187px;height:37px;font-size:12px}

/* thinking */
.intro-text{left:232px;top:838px;width:740px;font-size:12px;line-height:18px}
.reasons-list{top:900px;width:190px;font-size:12px;line-height:18px}
.reasons-list li{list-style:none;position:relative;padding-left:20px;margin-bottom:4px}
.reasons-list li::before{content:"";position:absolute;left:2px;top:3px;width:6px;height:10px;border:solid var(--green);border-width:0 2px 2px 0;transform:rotate(45deg)}
.photo-band{left:0;top:1080px;width:1200px;height:312px;background:linear-gradient(90deg,#f2f2f2 0%,#e6e6e6 45%,#c9c9c4 70%,#ededed 100%)}

/* benefit icons */
.ring{position:absolute;border:2px solid var(--blue);border-radius:50%;display:flex;align-items:center;justify-content:center}
.ring.green{border-color:var(--green)}
.icon-label{position:absolute;font-size:12px;text-align:center;width:160px;line-height:16px}

.cta-band{left:0;top:1977px;width:1200px;height:188px;background:linear-gradient(90deg,#97c07c 0%,#8eb3a0 50%,#7198b8 100%)}
.video{left:360px;top:2550px;width:480px;height:250px;background:linear-gradient(135deg,#1a5aa7 0%,#2e7c9e 60%,#2a9a6e 100%)}

/* reviews */
.reviews-band{left:0;top:2862px;width:1200px;height:1018px;background:var(--band)}
.quote-mark{font-size:90px;color:#c4c4c4;line-height:1}
.review-card{position:absolute;width:358px;height:220px;background:var(--white);border:1px solid #ddd;box-shadow:0 2px 6px rgba(0,0,0,.15);text-align:center}
.avatar{width:62px;height:62px;border-radius:50%;background:linear-gradient(180deg,#8a95a5,#39465a);margin:14px auto 4px}
.reviewer{font-size:12px}
.stars{color:#f0b400;font-size:9px;letter-spacing:1px}
.review-text{font-size:9px;line-height:13px;text-align:left;padding:6px 44px 0 44px}
.review-date{position:absolute;right:48px;bottom:18px;font-size:6px;color:var(--muted)}

/* faq */
.faq{left:232px;width:736px}
.faq-row{height:29px;border-bottom:1px solid var(--line);font-size:12px;display:flex;justify-content:space-between;align-items:center}
.caret{width:0;height:0;border-left:4px solid transparent;border-right:4px solid transparent;border-top:5px solid var(--ink)}

/* form */
.field{position:absolute;font-size:12px;border-bottom:1px solid var(--green);height:24px}
.field b{color:var(--blue);font-weight:400}

/* footer */
.site-footer{left:0;top:4770px;width:1200px;height:230px;background:var(--footer)}
.foot-col{position:absolute;font-size:9px;line-height:12px}
.foot-col h3{font-size:9px;font-weight:400;margin-bottom:20px}
.social{display:flex;gap:10px;margin-top:2px}
.social span{width:9px;height:9px;border-radius:50%;background:var(--ink)}
</style>
</head>
<body>

<header class="abs site-header">
  <div class="abs" style="left:232px;top:22px">
    <div class="brand"><span class="brand-name">TREVLO</span><span class="brand-mark"></span></div>
    <div class="brand-tag">HOME BUYERS</div>
  </div>
  <div class="abs top-phone">
    <svg width="10" height="10" viewBox="0 0 10 10"><circle cx="5" cy="5" r="5" fill="#6bb02a"/><path d="M3.2 2.6l1 .9-.5.8c.4.8 1 1.4 1.8 1.8l.8-.5.9 1-.7.9C4.8 7.3 2.8 5.3 2.6 3.4z" fill="#fff"/></svg>
    (555) 014-2290
  </div>
  <nav class="abs main-nav">
    <span>Home</span><span>Why Trevlo Home Buyers</span><span>How It Works</span><span>Reasons to Sell</span><span>Locations</span><span>FAQ</span><span>Contact</span>
  </nav>
</header>

<section class="abs hero" role="img" aria-label="Photo of a two-storey suburban house with a white picket fence under a blue sky"></section>
<h1 class="abs center hero-title">We Buy Homes From People in a Trevlo!</h1>
<p class="abs center hero-sub">Get your cash offer today.</p>
<div class="abs address-field">
  <svg width="10" height="13" viewBox="0 0 10 13"><path d="M5 0a5 5 0 0 1 5 5c0 3.5-5 8-5 8S0 8.5 0 5a5 5 0 0 1 5-5z" fill="#fff"/><circle cx="5" cy="5" r="1.8" fill="#33506f"/></svg>
  Enter Your Street Address
</div>
<div class="btn offer-btn">Get A Cash Offer</div>

<h2 class="abs center section-title" style="top:745px">Thinking of Selling?</h2>
<p class="abs intro-text">No matter your situation, we will buy your home. No need to worry about the condition of the house either - we'll make this a stress-free process and get you cash quickly.</p>
<ul class="abs reasons-list" style="left:232px"><li>Retirement -</li><li>Inheritance - Have you inherited a home and you don't want to worry about the headache that comes with it? Sell it to the Trevlo Home Experts!</li></ul>
<ul class="abs reasons-list" style="left:420px"><li>Downsizing or Upsizing -</li><li>Massive Repairs - Is your home too much to manage? No problem; our team is happy to take it off your hands.</li></ul>
<ul class="abs reasons-list" style="left:615px"><li>Divorce -</li><li>Moving - Sometimes you just want to move and that's okay too! Let us help you get into your dream home.</li></ul>
<ul class="abs reasons-list" style="left:810px"><li>Probate -</li><li>Bad Mortgage - Selling your home is a great way to get out of your current mortgage quick.</li></ul>

<div class="abs photo-band" role="img" aria-label="Photo of a thoughtful man holding a small model house on his palm"></div>
<div class="btn" style="left:521px;top:1425px;width:158px;height:37px">More Reasons to Sell</div>

<h2 class="abs center section-title" style="top:1582px">Reasons People Work with Trevlo</h2>
<p class="abs center section-sub" style="top:1672px">Benefits of working with us over a realtor.</p>

<div class="ring" style="left:239px;top:1725px;width:97px;height:97px"><svg width="44" height="44" viewBox="0 0 44 44" fill="none" stroke="#1e1e1e" stroke-width="2"><circle cx="26" cy="25" r="12"/><path d="M26 25l5-5M23 10h6M26 10v3"/><path d="M4 20h8M2 26h9M5 32h8" stroke="#6bb02a"/></svg></div>
<div class="icon-label" style="left:208px;top:1836px">Quick Turnaround</div>
<div class="ring" style="left:444px;top:1725px;width:97px;height:97px"><svg width="44" height="44" viewBox="0 0 44 44" fill="none" stroke="#1e1e1e" stroke-width="2"><circle cx="22" cy="22" r="17"/><path d="M10 34L34 10"/><path d="M27 16c-2-2-9-2-9 2s9 3 9 7-7 4-9 2M22 12v20"/></svg></div>
<div class="icon-label" style="left:413px;top:1836px">Zero Fees</div>
<div class="ring" style="left:649px;top:1725px;width:97px;height:97px"><svg width="44" height="44" viewBox="0 0 44 44" fill="none" stroke="#1e1e1e" stroke-width="2"><path d="M22 4l4 4 6-1 1 6 5 3-3 5 3 5-5 3-1 6-6-1-4 4-4-4-6 1-1-6-5-3 3-5-3-5 5-3 1-6 6 1z"/><path d="M15 22l5 5 10-10" stroke="#6bb02a" stroke-width="3"/></svg></div>
<div class="icon-label" style="left:618px;top:1836px">Stress &amp; Hassle Free</div>
<div class="ring" style="left:854px;top:1725px;width:97px;height:97px"><svg width="46" height="44" viewBox="0 0 46 44" fill="none" stroke="#1e1e1e" stroke-width="2"><circle cx="30" cy="22" r="12" fill="#6bb02a" stroke="#1e1e1e"/><path d="M34 17c-2-2-7-2-7 1s7 2 7 5-5 3-7 1M30 14v16" stroke="#1e1e1e"/><path d="M4 18h12M2 22h14M6 26h10"/></svg></div>
<div class="icon-label" style="left:823px;top:1836px">Cold Hard Cash Fast</div>

<div class="abs cta-band"></div>
<h2 class="abs center" style="top:2018px;font-size:31px;color:var(--ink)">We're the experts you turn to in a trevlo.</h2>
<div class="btn" style="left:521px;top:2080px;width:158px;height:38px">GET STARTED</div>

<h2 class="abs center section-title" style="top:2284px">How It Works</h2>
<div class="ring green" style="left:237px;top:2373px;width:68px;height:68px"><svg width="32" height="32" viewBox="0 0 32 32" fill="none" stroke="#1b4f91" stroke-width="1.8"><rect x="4" y="8" width="24" height="16"/><path d="M4 8l12 10 12-10"/></svg></div>
<div class="icon-label" style="left:191px;top:2452px">Call or Email<br>Us</div>
<div class="ring green" style="left:401px;top:2373px;width:68px;height:68px"><svg width="32" height="32" viewBox="0 0 32 32" fill="none" stroke="#1b4f91" stroke-width="1.8"><path d="M12 6l3 6-3 2c1 3 3 5 6 6l2-3 6 3-2 5C15 25 7 17 7 8z" fill="#1b4f91"/></svg></div>
<div class="icon-label" style="left:355px;top:2452px">Speak to a<br>Trevlo Expert</div>
<div class="ring green" style="left:567px;top:2373px;width:68px;height:68px"><svg width="32" height="32" viewBox="0 0 32 32" fill="none" stroke="#1b4f91" stroke-width="1.8"><rect x="5" y="7" width="22" height="20" rx="2"/><path d="M5 12h22M10 4v5M22 4v5M10 17h3M15 17h3M20 17h3M10 21h3M15 21h3"/></svg></div>
<div class="icon-label" style="left:521px;top:2452px">Schedule a Quick<br>Walk-Through</div>
<div class="ring green" style="left:733px;top:2373px;width:68px;height:68px"><svg width="32" height="32" viewBox="0 0 32 32" fill="none" stroke="#1b4f91" stroke-width="1.8"><circle cx="19" cy="10" r="6"/><path d="M4 22h6l5 2h6l6-4M4 27h8l6 1 9-5"/></svg></div>
<div class="icon-label" style="left:687px;top:2452px">Receive a<br>Cash Offer</div>
<div class="ring green" style="left:898px;top:2373px;width:68px;height:68px"><svg width="32" height="32" viewBox="0 0 32 32" fill="none" stroke="#1b4f91" stroke-width="1.8"><circle cx="16" cy="16" r="11"/><circle cx="16" cy="16" r="8"/><path d="M11 16h10"/></svg></div>
<div class="icon-label" style="left:852px;top:2452px">Get Paid</div>

<div class="abs video" role="img" aria-label="Video cover showing a large house at dusk with a blue and green tint"></div>
<div class="abs center" style="top:2596px;font-size:19px;color:var(--white)">Close as Fast as 7 Days!</div>
<svg class="abs" style="left:570px;top:2648px" width="60" height="60" viewBox="0 0 60 60"><circle cx="30" cy="30" r="26" fill="none" stroke="#fff" stroke-width="4"/><path d="M24 18l18 12-18 12z" fill="#fff"/></svg>

<section class="abs reviews-band"></section>
<h2 class="abs center section-title" style="top:2918px">Reviews</h2>
<p class="abs center section-sub" style="top:3005px">Hear from satisfied sellers.</p>
<div class="abs quote-mark" style="left:152px;top:3000px">&ldquo;</div>
<div class="abs quote-mark" style="left:1012px;top:3700px">&rdquo;</div>

<article class="review-card" style="left:232px;top:3050px"><div class="avatar"></div><div class="reviewer">Dana</div><div class="stars">★★★★★</div><p class="review-text">"Smooth, easy, fast." I was hesitant of the whole deal, because it seemed too easy. And now that I'm at the final sale, if Marcus tells you he's doing it, he's doing it. It's that simple."</p><span class="review-date">6/25/2019</span></article>
<article class="review-card" style="left:608px;top:3050px"><div class="avatar"></div><div class="reviewer">John Doe</div><div class="stars">★★★★★</div><p class="review-text">"Lorem Ipsum is simply dummy text of the printing and typesetting industry. Lorem Ipsum has been the industry's standard dummy text ever since the 1500s, when an unknown printer took a galley of type and scrambled it to make a type specimen book."</p><span class="review-date">6/25/2019</span></article>
<article class="review-card" style="left:232px;top:3288px"><div class="avatar"></div><div class="reviewer">John Doe</div><div class="stars">★★★★★</div><p class="review-text">"Lorem Ipsum is simply dummy text of the printing and typesetting industry. Lorem Ipsum has been the industry's standard dummy text ever since the 1500s, when an unknown printer took a galley of type and scrambled it to make a type specimen book."</p><span class="review-date">6/25/2019</span></article>
<article class="review-card" style="left:608px;top:3288px"><div class="avatar"></div><div class="reviewer">John Doe</div><div class="stars">★★★★★</div><p class="review-text">"Lorem Ipsum is simply dummy text of the printing and typesetting industry. Lorem Ipsum has been the industry's standard dummy text ever since the 1500s, when an unknown printer took a galley of type and scrambled it to make a type specimen book."</p><span class="review-date">6/25/2019</span></article>
<article class="review-card" style="left:232px;top:3526px"><div class="avatar"></div><div class="reviewer">John Doe</div><div class="stars">★★★★★</div><p class="review-text">"Lorem Ipsum is simply dummy text of the printing and typesetting industry. Lorem Ipsum has been the industry's standard dummy text ever since the 1500s, when an unknown printer took a galley of type and scrambled it to make a type specimen book."</p><span class="review-date">6/25/2019</span></article>
<article class="review-card" style="left:608px;top:3526px"><div class="avatar"></div><div class="reviewer">John Doe</div><div class="stars">★★★★★</div><p class="review-text">"Lorem Ipsum is simply dummy text of the printing and typesetting industry. Lorem Ipsum has been the industry's standard dummy text ever since the 1500s, when an unknown printer took a galley of type and scrambled it to make a type specimen book."</p><span class="review-date">6/25/2019</span></article>
<div class="btn" style="left:521px;top:3779px;width:158px;height:37px">SEE MORE REVIEWS</div>

<h2 class="abs center section-title" style="top:3933px">Questions?</h2>
<p class="abs center section-sub" style="top:4027px">We have the answers.</p>
<div class="abs faq" style="top:4064px">
  <div class="faq-row">How fast does this work?<span class="caret"></span></div>
  <div class="faq-row">What are your fees?<span class="caret"></span></div>
  <div class="faq-row">What if my home is not in good shape?<span class="caret"></span></div>
</div>
<div class="btn" style="left:553px;top:4200px;width:94px;height:37px">More FAQs</div>

<h2 class="abs center section-title" style="top:4345px">Contact Us</h2>
<div class="field" style="left:232px;top:4432px;width:190px">Full Name <b>*</b></div>
<div class="field" style="left:441px;top:4432px;width:188px">Phone <b>*</b></div>
<div class="field" style="left:649px;top:4432px;width:208px">E-mail <b>*</b></div>
<div class="field" style="left:872px;top:4432px;width:96px">City <b>*</b></div>
<div class="field" style="left:232px;top:4478px;width:397px">Street Address <b>*</b></div>
<div class="field" style="left:649px;top:4478px;width:208px">State <b>*</b></div>
<div class="field" style="left:872px;top:4478px;width:96px">Zip <b>*</b></div>
<div class="field" style="left:232px;top:4526px;width:736px;height:104px">Message <b>*</b></div>
<div class="btn" style="left:521px;top:4637px;width:158px;height:38px">GET A CASH OFFER</div>

<footer class="abs site-footer">
  <div class="abs" style="left:232px;top:34px">
    <div class="brand"><span class="brand-name">TREVLO</span><span class="brand-mark"></span></div>
    <div class="brand-tag">HOME BUYERS</div>
  </div>
  <div class="abs top-phone" style="left:232px;top:132px;right:auto">
    <svg width="10" height="10" viewBox="0 0 10 10"><circle cx="5" cy="5" r="5" fill="#6bb02a"/><path d="M3.2 2.6l1 .9-.5.8c.4.8 1 1.4 1.8 1.8l.8-.5.9 1-.7.9C4.8 7.3 2.8 5.3 2.6 3.4z" fill="#fff"/></svg>
    (555) 014-2290
  </div>
  <div class="foot-col" style="left:446px;top:34px"><h3>Quick Links</h3>Home<br>Why Trevlo Home Buyers<br>How It Works<br>Reasons to Sell<br>Locations<br>FAQ<br>Contact</div>
  <div class="foot-col" style="left:676px;top:38px"><h3>Security</h3>Terms of use<br>Privacy policy<br>Trust &amp; Safety</div>
  <div class="foot-col" style="left:866px;top:34px"><h3 style="margin-bottom:12px">Follow Us</h3><div class="social"><span></span><span></span><span></span><span></span><span></span></div></div>
  <div class="abs center" style="top:212px;font-size:6px">Copyright © 2019 Trevlo</div>
</footer>

</body>
</html>
```